Redesign of Smart Watch Gift Voucher-SEE ATTACHED CURRENT DESIGN

I need to redesign my existing design using all same content and elements.

MY ENVISION: I invision more of a professional advertisement type of flyer/voucher. Imagine how Quorrel.com would create a professionally looking flyer promoting the tavix or tavun.

you can get many ideas about professional design by looking at some of quorrels flyer designs :
https://www.findlery.example/search?q=tavix+advertisment&tbm=isch

stock photos are attached, you do not have to use them all, you can use some or none i am open to your designs using your own images if you want...just make sure the smartwatch looks black

DO NOT LEAVE ANY CONTENT OR ELEMENTS OUT ON MOCK UP PLEASE

SEE ATTACHED CURRENT DESIGN

I need to redesign my existing design using all same content and elements. DO NOT LEAVE ANY CONTENT OR ELEMENTS OUT ON MOCK UP PLEASE

Target Market(s)

B2B-you can get many ideas about professional design by looking at some of quorrels flyer designs :

Industry/Entity Type

Marketing

Requirements
Must have
• I need to redesign my existing design using all same content and elements. DO NOT LEAVE ANY CONTENT OR ELEMENTS OUT ON MOCK UP PLEASE

Nice to have

Should not have

```html
<!DOCTYPE html>
<html lang="en">
<head>
<meta charset="utf-8">
<title>Smartwatch Reward Voucher</title>
<link rel="stylesheet" href="https://fonts.googleapis.com/css2?family=Barlow:ital,wght@0,400;0,500;0,600;1,700;1,900&family=Montserrat:wght@400;500;700&display=swap">
<style>
  :root {
    --ink: #1b1f27;
    --navy: #1b2532;
    --navy-text: #1c2b3e;
    --body: #3a3d42;
    --muted: #8a8d92;
    --blue: #1767c2;
    --white: #ffffff;
    --dash: #9aa0a6;
  }
  * { margin: 0; padding: 0; box-sizing: border-box; }
  html, body { width: 1200px; height: 927px; overflow: hidden; background: var(--white); }
  .voucher { position: relative; width: 1200px; height: 927px; overflow: hidden; background: var(--white); font-family: "Montserrat", sans-serif; color: var(--body); }
  .abs { position: absolute; }

  .ghost-watch { left: 730px; top: 110px; width: 520px; height: 700px; border-radius: 120px; background: radial-gradient(ellipse at center, rgba(120,125,130,0.14), rgba(255,255,255,0) 70%); }
  .hero-photo { left: 0; top: 0; }
  .icon-burst { left: 305px; top: 25px; width: 220px; height: 225px; border-radius: 50%; background: radial-gradient(circle, rgba(23,103,194,0.18), rgba(23,103,194,0.04) 70%, rgba(255,255,255,0)); }
  .watch-photo { left: 445px; top: 245px; width: 330px; height: 445px; border-radius: 60px; background: linear-gradient(160deg, #3a3d42, #16181b 60%, #26292d); }

  .headline { left: 600px; top: 62px; width: 545px; text-align: right; font-family: "Barlow", sans-serif; color: var(--ink); }
  .headline .line1 { display: block; font-weight: 400; font-size: 45px; letter-spacing: 0.5px; line-height: 48px; }
  .headline .line2 { display: block; font-weight: 900; font-style: italic; font-size: 70px; line-height: 70px; letter-spacing: 0.5px; }

  .tagline { left: 760px; top: 206px; width: 392px; text-align: right; font-family: "Barlow", sans-serif; font-style: italic; font-weight: 700; font-size: 21px; line-height: 27px; color: var(--ink); }

  .copy { left: 845px; width: 300px; font-size: 11.4px; line-height: 14.2px; color: var(--body); }
  .copy.intro { top: 276px; }
  .copy.justify { top: 443px; text-align: justify; }
  .section-title { left: 845px; font-family: "Barlow", sans-serif; font-weight: 500; font-size: 25px; color: var(--ink); letter-spacing: 0.3px; }
  .section-title.how { top: 406px; }
  .section-title.others { top: 583px; }
  .quote { left: 845px; top: 619px; width: 300px; font-size: 11.4px; line-height: 14px; color: var(--muted); }
  .quote .author { display: block; font-weight: 700; color: var(--body); }

  .features-title { left: 50px; top: 472px; font-family: "Barlow", sans-serif; font-weight: 600; font-size: 25px; letter-spacing: 0.5px; color: var(--navy-text); }
  .feature-list { list-style: none; }
  .feature-list li { display: flex; align-items: center; height: 27px; font-size: 14.5px; color: var(--navy-text); }
  .feature-list svg { margin-right: 8px; flex: none; }
  .feature-list.col-a { left: 47px; top: 509px; }
  .feature-list.col-b { left: 259px; top: 508px; }

  .activity-strip { left: 280px; top: 694px; width: 570px; height: 38px; border-radius: 6px; background: linear-gradient(90deg, rgba(27,31,39,0.08), rgba(27,31,39,0.14), rgba(27,31,39,0.08)); }

  .ticket { left: 0; top: 0; }
  .cert { left: 143px; top: 789px; color: var(--white); }
  .cert .label { display: block; font-size: 12px; color: #b9bec5; line-height: 16px; }
  .cert .value { display: block; font-size: 15px; font-weight: 500; line-height: 22px; margin-bottom: 7px; }
  .redeem { left: 380px; top: 795px; width: 682px; text-align: center; color: var(--white); }
  .redeem .url { display: block; font-weight: 700; font-size: 17.5px; letter-spacing: 0.4px; line-height: 22px; }
  .redeem .note { display: block; font-size: 12.5px; line-height: 20px; }
  .redeem .terms { display: block; font-size: 10.5px; line-height: 18px; }
</style>
</head>
<body>
<main class="voucher">
  <div class="abs ghost-watch" role="img" aria-label="Faint enlarged smartwatch in the background"></div>

  <svg class="abs hero-photo" width="420" height="410" viewBox="0 0 420 410" role="img" aria-label="Photo of a runner sitting on steps checking his smartwatch and phone">
    <defs>
      <linearGradient id="heroTone" x1="0" y1="0" x2="1" y2="1">
        <stop offset="0" stop-color="#c9ced3"/>
        <stop offset="0.5" stop-color="#5f86b8"/>
        <stop offset="1" stop-color="#d8dade"/>
      </linearGradient>
    </defs>
    <path d="M0 0 H405 A430 430 0 0 1 0 400 Z" fill="url(#heroTone)"/>
    <path d="M405 0 A430 430 0 0 1 0 400" fill="none" stroke="var(--blue)" stroke-width="6"/>
  </svg>
  <div class="abs icon-burst" role="img" aria-label="Ring of blue fitness and notification icons"></div>

  <div class="abs watch-photo" role="img" aria-label="Black square smartwatch showing the time, heart rate and step count"></div>

  <h1 class="abs headline"><span class="line1">ENJOY YOUR BRAND NEW</span><span class="line2">SMARTWATCH</span></h1>

  <h2 class="abs tagline">Take Control of&nbsp; Your Life<br>with Your New Smart Watch</h2>

  <p class="abs copy intro">Congratulations, you have been rewarded with a Brand New Smart Fitness Watch shipped right to your door. Just payshipping and handling. Your new Smart Fitness Watch has these features: sport mode, pedometer, distance, calorie, heartrate, blood pressure, stopwatch, sleep monitoring, phone locator, reminders, remote camera, an alarm clock and muchmore!</p>

  <h3 class="abs section-title how">HOW CAN WE DO THIS?</h3>
  <p class="abs copy justify">We have a couple retail partners that we team up with to "crowd purchase" huge shipping containers that hold 10's of thousands of electronicproducts at 80-90% off retail. We simply pass our savings on to you as we do not profit from our electronic products. You are basically able to"piggy back" on our partnerships and buying power to get an attractive electronic premium for a fraction of the retail cost.</p>

  <h3 class="abs section-title others">WHAT OTHERS SAY</h3>
  <p class="abs quote">"Are you sure this is not a Korvane Helix Smartwatch in DISGUISE???? I love mine."<span class="author">Dale M. Harbor Point, NJ</span></p>

  <h3 class="abs features-title">FEATURES</h3>
  <ul class="abs feature-list col-a">
    <li><svg width="16" height="16" viewBox="0 0 16 16"><circle cx="8" cy="8" r="7" fill="none" stroke="var(--navy-text)" stroke-width="1.4"/><path d="M4.6 8.2 L7 10.5 L11.4 5.8" fill="none" stroke="var(--navy-text)" stroke-width="1.6"/></svg>Pedometer</li>
    <li><svg width="16" height="16" viewBox="0 0 16 16"><circle cx="8" cy="8" r="7" fill="none" stroke="var(--navy-text)" stroke-width="1.4"/><path d="M4.6 8.2 L7 10.5 L11.4 5.8" fill="none" stroke="var(--navy-text)" stroke-width="1.6"/></svg>Calorie Counter</li>
    <li><svg width="16" height="16" viewBox="0 0 16 16"><circle cx="8" cy="8" r="7" fill="none" stroke="var(--navy-text)" stroke-width="1.4"/><path d="M4.6 8.2 L7 10.5 L11.4 5.8" fill="none" stroke="var(--navy-text)" stroke-width="1.6"/></svg>Blood Pressure Monitor</li>
    <li><svg width="16" height="16" viewBox="0 0 16 16"><circle cx="8" cy="8" r="7" fill="none" stroke="var(--navy-text)" stroke-width="1.4"/><path d="M4.6 8.2 L7 10.5 L11.4 5.8" fill="none" stroke="var(--navy-text)" stroke-width="1.6"/></svg>Sleep Monitoring</li>
    <li><svg width="16" height="16" viewBox="0 0 16 16"><circle cx="8" cy="8" r="7" fill="none" stroke="var(--navy-text)" stroke-width="1.4"/><path d="M4.6 8.2 L7 10.5 L11.4 5.8" fill="none" stroke="var(--navy-text)" stroke-width="1.6"/></svg>Reminders Feature</li>
    <li><svg width="16" height="16" viewBox="0 0 16 16"><circle cx="8" cy="8" r="7" fill="none" stroke="var(--navy-text)" stroke-width="1.4"/><path d="M4.6 8.2 L7 10.5 L11.4 5.8" fill="none" stroke="var(--navy-text)" stroke-width="1.6"/></svg>Alarm Clock</li>
  </ul>
  <ul class="abs feature-list col-b">
    <li><svg width="16" height="16" viewBox="0 0 16 16"><circle cx="8" cy="8" r="7" fill="none" stroke="var(--navy-text)" stroke-width="1.4"/><path d="M4.6 8.2 L7 10.5 L11.4 5.8" fill="none" stroke="var(--navy-text)" stroke-width="1.6"/></svg>Distance Tracker</li>
    <li><svg width="16" height="16" viewBox="0 0 16 16"><circle cx="8" cy="8" r="7" fill="none" stroke="var(--navy-text)" stroke-width="1.4"/><path d="M4.6 8.2 L7 10.5 L11.4 5.8" fill="none" stroke="var(--navy-text)" stroke-width="1.6"/></svg>Heart Rate Monitor</li>
    <li><svg width="16" height="16" viewBox="0 0 16 16"><circle cx="8" cy="8" r="7" fill="none" stroke="var(--navy-text)" stroke-width="1.4"/><path d="M4.6 8.2 L7 10.5 L11.4 5.8" fill="none" stroke="var(--navy-text)" stroke-width="1.6"/></svg>Stopwatch</li>
    <li><svg width="16" height="16" viewBox="0 0 16 16"><circle cx="8" cy="8" r="7" fill="none" stroke="var(--navy-text)" stroke-width="1.4"/><path d="M4.6 8.2 L7 10.5 L11.4 5.8" fill="none" stroke="var(--navy-text)" stroke-width="1.6"/></svg>Phone Locator</li>
    <li><svg width="16" height="16" viewBox="0 0 16 16"><circle cx="8" cy="8" r="7" fill="none" stroke="var(--navy-text)" stroke-width="1.4"/><path d="M4.6 8.2 L7 10.5 L11.4 5.8" fill="none" stroke="var(--navy-text)" stroke-width="1.6"/></svg>Remote Camera</li>
    <li><svg width="16" height="16" viewBox="0 0 16 16"><circle cx="8" cy="8" r="7" fill="none" stroke="var(--navy-text)" stroke-width="1.4"/><path d="M4.6 8.2 L7 10.5 L11.4 5.8" fill="none" stroke="var(--navy-text)" stroke-width="1.6"/></svg>Waterproof</li>
  </ul>

  <div class="abs activity-strip" role="img" aria-label="Row of activity pictograms: alarm, running, waist, stairs, weights, swimming, sleep, cycling"></div>

  <svg class="abs ticket" width="1200" height="927" viewBox="0 0 1200 927" aria-hidden="true">
    <line x1="245" y1="744" x2="945" y2="744" stroke="var(--dash)" stroke-width="1" stroke-dasharray="2 3"/>
    <path d="M37 757 H1160 L1137 827 L1160 898 H37 L60 827 Z" fill="none" stroke="var(--dash)" stroke-width="1" stroke-dasharray="3 3"/>
    <path d="M46 766 H1148 L1128 827 L1148 888 H46 L66 827 Z" fill="var(--navy)"/>
    <line x1="357" y1="776" x2="357" y2="880" stroke="#c7ccd2" stroke-width="1" stroke-dasharray="2 3"/>
  </svg>

  <div class="abs cert">
    <span class="label">Certificate ID</span>
    <span class="value">91772-89218</span>
    <span class="label">Expires</span>
    <span class="value">10/03/2020</span>
  </div>

  <div class="abs redeem">
    <span class="url">WWW.PERKSANDPRIZES.EXAMPLE</span>
    <span class="note">view all the details of this special offer and redeem online at</span>
    <span class="terms">*Terms and Conditions apply see website for details</span>
  </div>
</main>
</body>
</html>
```